Sales Brochure

Industrial brochure of my industrial pump business which includes repair and sales of equipment. I distribute and repair industrial pumps for the midwest market. Design color is blue.

```html
<!DOCTYPE html>
<html lang="en">
<head>
<meta charset="utf-8">
<title>Lakeside Pump – Folding Brochure</title>
<link href="https://fonts.googleapis.com/css2?family=Roboto+Condensed:wght@400;700&family=Source+Sans+3:wght@400&family=Kalam:wght@400&display=swap" rel="stylesheet">
<style>
  :root{
    --stage:#c5dbee;
    --sheet:#f1f6fc;
    --sheet-soft:#e6eff9;
    --blue-deep:#3f6fc4;
    --blue-mid:#5b8fd6;
    --blue-light:#8cc4ec;
    --ink:#1d1d1f;
    --white:#ffffff;
  }
  *{margin:0;padding:0;box-sizing:border-box}
  html,body{width:1200px;height:1200px;overflow:hidden;background:var(--stage)}
  .canvas{position:relative;width:1200px;height:1200px;background:var(--stage);font-family:"Source Sans 3",sans-serif;color:var(--ink)}

  .spread{position:absolute;left:283px;width:634px;height:490px;overflow:hidden}
  .spread--outside{top:91px;background:var(--sheet)}
  .spread--inside{top:619px;background:var(--sheet-soft)}

  .repair-caption{position:absolute;left:330px;top:0;width:222px;top:36px;left:47px;text-align:center;font-size:11.5px;line-height:15px}
  .product-photo{position:absolute;background:linear-gradient(150deg,#6f86b8,#2f4fa8 60%,#8a8f99)}
  .product-photo--red{background:linear-gradient(150deg,#a65a4d,#c7272d 55%,#6b5d57)}
  .product-photo--grey{background:linear-gradient(150deg,#9aa0a8,#6c737c 55%,#8a7a66)}
  .product-photo--white{background:linear-gradient(150deg,#d9dde2,#2c2f36 55%,#b8bcc2)}

  .headline{position:absolute;left:336px;top:25px;font-family:"Roboto Condensed",sans-serif;font-weight:700;font-size:13.5px;line-height:16.5px}
  .decor-bloom{position:absolute;right:-120px;top:30px;width:300px;height:300px;border-radius:50%;background:radial-gradient(circle at 35% 60%,var(--blue-light),var(--blue-mid) 55%,var(--blue-deep))}
  .brand{position:absolute;left:390px;top:373px;display:flex;align-items:center;gap:6px}
  .brand-dot{width:26px;height:26px;border-radius:50%;background:var(--blue-mid)}
  .brand-name{font-family:"Roboto Condensed",sans-serif;font-weight:700;font-size:19px;color:var(--blue-deep);letter-spacing:.3px}

  .contact-band{position:absolute;left:0;bottom:0;width:634px;height:25px;background:linear-gradient(90deg,var(--blue-deep),var(--blue-mid) 35%,var(--blue-light) 55%,var(--blue-mid) 75%,var(--blue-deep))}
  .contact-phone{position:absolute;left:104px;top:5px;font-family:"Roboto Condensed",sans-serif;font-weight:700;font-size:11.5px;color:var(--white)}
  .contact-web{position:absolute;left:414px;top:4px;font-family:"Kalam",cursive;font-size:10.5px;color:var(--white)}

  .section-tag{position:absolute;height:17px;background:linear-gradient(90deg,var(--blue-deep),var(--blue-mid) 70%,var(--blue-light));clip-path:polygon(0 0,100% 0,92% 100%,0 100%);color:var(--white);font-size:11.5px;line-height:17px;padding-left:28px}
  .section-body{position:absolute;font-size:11.4px;line-height:14.4px;text-align:justify;hyphens:auto}

  .fade-photo{position:absolute;left:0;top:313px;width:317px;height:177px;background:linear-gradient(180deg,var(--sheet-soft),#9db4e0 40%,#3d58b8)}
  .plant-photo{position:absolute;left:317px;top:0;width:317px;height:250px;background:linear-gradient(135deg,#1f3f9a,#3d7fd0 40%,#2aa79e 75%,#cfe3f2)}

  .format-note{position:absolute;left:970px;top:1062px;font-size:17px;line-height:23px}
</style>
</head>
<body>
<div class="canvas">

  <section class="spread spread--outside">
    <p class="repair-caption">We offer repair services for<br>all the equipment we sell</p>
    <div class="product-photo" style="left:41px;top:89px;width:55px;height:113px" role="img" aria-label="Vertical multistage pump"></div>
    <div class="product-photo" style="left:100px;top:89px;width:85px;height:113px" role="img" aria-label="Blue split-case pump on a pallet"></div>
    <div class="product-photo" style="left:188px;top:89px;width:87px;height:113px" role="img" aria-label="Rows of blue pump housings"></div>
    <div class="product-photo" style="left:39px;top:205px;width:146px;height:114px" role="img" aria-label="Blue self-priming pump"></div>
    <div class="product-photo product-photo--red" style="left:188px;top:205px;width:87px;height:114px" role="img" aria-label="Red vertical turbine pump head"></div>
    <div class="product-photo product-photo--grey" style="left:39px;top:319px;width:145px;height:102px" role="img" aria-label="Grey sump pump on a pallet"></div>
    <div class="product-photo product-photo--white" style="left:186px;top:319px;width:90px;height:102px" role="img" aria-label="White diaphragm pump"></div>

    <h1 class="headline">Our industrial<br>equipment keeps<br>your business<br>moving forward.</h1>
    <div class="decor-bloom" role="img" aria-label="Soft blue decorative shape"></div>
    <div class="brand"><span class="brand-dot"></span><span class="brand-name">LAKESIDE PUMP</span></div>

    <div class="contact-band">
      <span class="contact-phone">Main Ph:&nbsp; 555-014-2387</span>
      <span class="contact-web">www.lakesidepump.com</span>
    </div>
  </section>

  <section class="spread spread--inside">
    <h2 class="section-tag" style="left:0;top:26px;width:108px;font-weight:400">Our Vision</h2>
    <p class="section-body" style="left:28px;top:57px;width:254px">At Lakeside Pump, our vision is to be the leading provider of industrial equipment in the country. We are committed to providing our clients with the highest quality products and services to help them succeed and grow. We will achieve this by staying at the forefront of industry trends and by continuously improving our offerings.</p>

    <h2 class="section-tag" style="left:0;top:171px;width:108px;font-weight:400">Our Products</h2>
    <p class="section-body" style="left:28px;top:202px;width:254px">We offer a comprehensive range of industrial equipment, including pumps, motors, and power transmission products. All of our products are sourced from trusted brands and are of the highest quality. We are dedicated to providing our clients with reliable, durable, and efficient equipment.</p>

    <div class="fade-photo" role="img" aria-label="Faded photo of a blue self-priming pump"></div>
    <div class="plant-photo" role="img" aria-label="Industrial pump room with pipes, valves and gauges"></div>

    <h2 class="section-tag" style="left:319px;top:296px;width:108px;font-weight:400;padding-left:17px">Our Expertise</h2>
    <p class="section-body" style="left:336px;top:327px;width:256px">With over 78 years of combined experience in the industrial equipment industry, the team at Lakeside Pump has the knowledge and expertise to help you find the right equipment for your business needs. We offer expert advice, personalized service, and ongoing support to ensure your complete satisfaction.</p>
  </section>

  <p class="format-note">A4 Size<br>Folding Brochoure</p>
</div>
</body>
</html>
```